Ma V's -100% Juice -Can Design - 8 Varieties

We are looking for to design our new range of 100% Juices which are made in Vietnam and will be imported into Australia.
Our New Brand is to be called “Ma V’s” or "Ma V's Juices"
We will initially have 8 products in the range. Our range of 100% juices will be packed in 500ml Aluminium Cans.
We envisage to have the same general/consistent branding on each can but with different fruit images of all the different juice varieties to be a main part for the image. I have attached a couple of samples of Juice design so you can use a reference point.
We will have the following varieties in our Juice range:
Pineapple
Mango
Passion fruit
Lychee
Pink Guava
Watermelon
Coconut Water
Coconut Water with Chocolate
We have done a few designs for the branding of "Ma V’s” which are attached below but we are happy if they are modified/adjusted to fit in with the overall design of the can.
The design needs to state:
“100% Natural”
“No Added Sugar”
“Never from Concentrate”
“Made from Whole fruit”
The back of the can will need a Nutritional Panel, Ingredient list and must have a barcode.
Image below attached with requirements needed for Australia.
The cans must look striking so they stand out and elegant and sophisticated.

```html
<!DOCTYPE html>
<html lang="en">
<head>
<meta charset="utf-8">
<title>Ma V's Juices – Can Labels</title>
<link rel="stylesheet" href="https://fonts.googleapis.com/css2?family=Oswald:wght@500&family=Marcellus+SC&family=Gentium+Book+Plus&display=swap">
<style>
  :root {
    --backdrop: #1f1e1c;
    --label-cream: #ebe4d4;
    --leaf-green: #2f6a3a;
    --ink-dark: #2a2622;
    --passion: #c2479f;
    --passion-band: #d66cc0;
    --lychee: #d9476a;
    --lychee-band: #e45b7a;
    --mango: #e9952a;
    --mango-band: #f0a53a;
  }
  * { margin: 0; padding: 0; box-sizing: border-box; }
  html, body { width: 1200px; height: 800px; overflow: hidden; }
  body { background: var(--backdrop); position: relative; }

  .can-label {
    position: absolute;
    top: 196px;
    width: 193px;
    height: 472px;
    background: var(--label-cream);
    border-radius: 6px;
    overflow: hidden;
    text-align: center;
    color: var(--ink-dark);
  }
  .can-label--passion { left: 278px; --accent: var(--passion); --band: var(--passion-band); --art-a: #7a2e5a; --art-b: #f0b83a; }
  .can-label--lychee  { left: 511px; --accent: var(--lychee);  --band: var(--lychee-band);  --art-a: #c9344f; --art-b: #f3c9cf; }
  .can-label--mango   { left: 743px; --accent: var(--mango);   --band: var(--mango-band);   --art-a: #f0a320; --art-b: #4f8a3c; }

  .top-band { position: absolute; top: 0; left: 0; width: 193px; height: 70px; }
  .top-band path { fill: var(--band); }
  .natural-claim {
    position: absolute; top: 13px; left: 0; right: 0;
    font-family: "Gentium Book Plus", serif;
    font-size: 15px; letter-spacing: 0.5px; color: #fbf4ea;
  }
  .brand-name {
    position: absolute; top: 80px; left: 0; right: 0;
    font-family: "Marcellus SC", serif;
    font-size: 32px; color: var(--accent);
  }
  .fruit-art {
    position: absolute; top: 132px; left: 26px; width: 141px; height: 160px;
    border-radius: 50%;
    background: radial-gradient(circle at 50% 55%, var(--art-a) 0%, var(--art-b) 60%, rgba(235,228,212,0) 75%);
  }
  .flavour-name {
    position: absolute; top: 290px; left: 0; right: 0;
    font-family: "Oswald", sans-serif; font-weight: 500;
    font-size: 38px; line-height: 1; letter-spacing: -0.5px;
    color: var(--accent); transform: scaleY(1.1);
  }
  .can-label--passion .flavour-name { font-size: 33px; }
  .juice-word {
    position: absolute; top: 336px; left: 0; right: 0;
    font-family: "Marcellus SC", serif; font-size: 20px; letter-spacing: 2px;
    color: var(--leaf-green);
  }
  .rule {
    position: absolute; left: 80px; width: 33px; height: 1px; background: var(--accent);
  }
  .rule--upper { top: 366px; }
  .rule--lower { top: 423px; }
  .no-word {
    position: absolute; top: 370px; left: 0; right: 0;
    font-family: "Marcellus SC", serif; font-size: 19px; color: var(--leaf-green);
  }
  .claim-lines {
    position: absolute; top: 393px; left: 0; right: 0;
    font-family: "Marcellus SC", serif; font-size: 10px; line-height: 11px;
  }
  .whole-fruit {
    position: absolute; top: 430px; left: 0; right: 0;
    font-family: "Marcellus SC", serif; font-size: 9px; letter-spacing: 0.5px;
  }
  .volume {
    position: absolute; top: 447px; left: 0; right: 0;
    font-family: "Gentium Book Plus", serif; font-size: 12.5px; letter-spacing: 0.4px;
  }
</style>
</head>
<body>

<section class="can-label can-label--passion">
  <svg class="top-band" viewBox="0 0 193 70" aria-hidden="true"><path d="M0 0H193V55C160 42 130 44 100 56C70 68 30 72 0 68Z"/></svg>
  <p class="natural-claim">100% Natural</p>
  <p class="brand-name">Ma V's</p>
  <div class="fruit-art" role="img" aria-label="Illustration of halved passion fruits with leaves and a golden juice splash"></div>
  <p class="flavour-name">PASSION FRUIT</p>
  <p class="juice-word">JUICE</p>
  <span class="rule rule--upper"></span>
  <p class="no-word">NO</p>
  <p class="claim-lines">ADDED SUGAR<br>FROM CONCENTRATE</p>
  <span class="rule rule--lower"></span>
  <p class="whole-fruit">MADE FROM WHOLE FRUIT</p>
  <p class="volume">500 ml/16.9 fl oz</p>
</section>

<section class="can-label can-label--lychee">
  <svg class="top-band" viewBox="0 0 193 70" aria-hidden="true"><path d="M0 0H193V55C160 42 130 44 100 56C70 68 30 72 0 68Z"/></svg>
  <p class="natural-claim">100% Natural</p>
  <p class="brand-name">Ma V's</p>
  <div class="fruit-art" role="img" aria-label="Illustration of lychees, one peeled, with leaves and a pink juice splash"></div>
  <p class="flavour-name">LYCHEE</p>
  <p class="juice-word">JUICE</p>
  <span class="rule rule--upper"></span>
  <p class="no-word">NO</p>
  <p class="claim-lines">ADDED SUGAR<br>FROM CONCENTRATE</p>
  <span class="rule rule--lower"></span>
  <p class="whole-fruit">MADE FROM WHOLE FRUIT</p>
  <p class="volume">500 ml/16.9 fl oz</p>
</section>

<section class="can-label can-label--mango">
  <svg class="top-band" viewBox="0 0 193 70" aria-hidden="true"><path d="M0 0H193V55C160 42 130 44 100 56C70 68 30 72 0 68Z"/></svg>
  <p class="natural-claim">100% Natural</p>
  <p class="brand-name">Ma V's</p>
  <div class="fruit-art" role="img" aria-label="Illustration of a cubed mango half with leaves and an orange juice splash"></div>
  <p class="flavour-name">MANGO</p>
  <p class="juice-word">JUICE</p>
  <span class="rule rule--upper"></span>
  <p class="no-word">NO</p>
  <p class="claim-lines">ADDED SUGAR<br>FROM CONCENTRATE</p>
  <span class="rule rule--lower"></span>
  <p class="whole-fruit">MADE FROM WHOLE FRUIT</p>
  <p class="volume">500 ml/16.9 fl oz</p>
</section>

</body>
</html>
```